Postcard Design

The Amberly Courier ~ Your #1 Newspaper since 1971

I am trying to reach new clients with our special of
Receive 1 month free with a year contract.

The Amberly Courier is a monthly newspaper that readers cherish like a magazine waiting for the next one to be published. I have had several advertisers since the first paper in 1971. My mom was the prior owner and she loved roosters, hence the rooster in the logo.

Please add the following:

Your # 1 Newspaper 

Serving Hollin County since 1971

1 Month FREE with 1 Year Contract

Instead of your #1 Newspaper...please put

The areas best place to see what's happening locally.

Target Market(s)

professionals, restaurants, etc.

Colors
33b7a4
85cae6
33a6d7

Requirements
Must have
• P.O. Box 417, Westbrook Mills, NJ 08652
Email: info@amberlycourier-example.com
609.555.0148
www.amberlycourier-example.com
Nice to have
• Typical savings up to $300.

```html
<!DOCTYPE html>
<html lang="en">
<head>
<meta charset="utf-8">
<title>The Amberly Courier – Postcard</title>
<link href="https://fonts.googleapis.com/css2?family=Arimo:wght@400;700&family=Tinos:wght@400;700&display=swap" rel="stylesheet">
<style>
  :root {
    --page-bg: #ece8e3;
    --card-white: #ffffff;
    --photo-light: #fbd9a6;
    --photo-mid: #f1a45a;
    --photo-dark: #3a2a22;
    --curve-band: #2e221d;
    --headline-orange: #f08a1c;
    --ink: #111111;
    --ink-soft: #2b2b2b;
    --copy-grey: #8a8a8a;
    --accent-orange: #e98b1e;
    --accent-blue: #4a78c4;
    --brand-teal: #33b7a4;
    --brand-sky: #85cae6;
    --brand-blue: #33a6d7;
    --panel-grey: #cfcfcf;
    --office-light: #d9dde2;
    --office-dark: #3b3f4a;
    --divider: #c8c8c8;
  }
  * { box-sizing: border-box; margin: 0; padding: 0; }
  html, body { width: 1200px; height: 533px; overflow: hidden; }
  body { background: var(--page-bg); position: relative; font-family: "Arimo", Arial, sans-serif; }

  .postcard {
    position: absolute; top: 44px; width: 553px; height: 428px;
    background: var(--card-white); overflow: hidden;
    box-shadow: 0 2px 8px rgba(0,0,0,.25);
  }
  .postcard--front { left: 43px; }
  .postcard--back { left: 611px; }

  /* Front */
  .front-art { position: absolute; inset: 0; }
  .front-headline {
    position: absolute; left: 16px; top: 20px;
    font: 700 32px/40px "Arimo", Arial, sans-serif; color: var(--headline-orange);
    text-shadow: 1px 2px 2px rgba(80,40,0,.35); letter-spacing: .5px;
  }
  .front-subline {
    position: absolute; left: 14px; top: 160px;
    font: 400 24px/31px "Arimo", Arial, sans-serif; color: var(--ink);
  }
  .front-offer {
    position: absolute; left: 14px; top: 232px;
    padding: 4px 12px; border-radius: 14px;
    background: var(--brand-blue); border: 2px solid var(--brand-sky);
    font: 700 16px/1.2 "Arimo", Arial, sans-serif; color: var(--card-white);
    white-space: nowrap;
  }
  .front-call {
    position: absolute; left: 12px; top: 298px;
    font: 400 21px/1 "Tinos", "Times New Roman", serif; font-variant: small-caps; color: var(--ink-soft);
  }
  .front-phone {
    position: absolute; left: 10px; top: 328px;
    font: 400 41px/1 "Tinos", "Times New Roman", serif; color: var(--ink-soft);
  }
  .front-web {
    position: absolute; left: 12px; top: 379px;
    font: 400 20px/1 "Tinos", "Times New Roman", serif; color: var(--ink-soft);
  }
  .brand-mark {
    position: absolute; left: 340px; top: 374px;
    display: flex; align-items: center; gap: 7px; white-space: nowrap;
    font: 700 20px/1 "Tinos", "Times New Roman", serif; color: var(--brand-teal);
  }
  .brand-mark__dot { width: 13px; height: 13px; border-radius: 50%; background: var(--brand-blue); flex: none; }

  /* Back */
  .back-panel {
    position: absolute; left: 0; top: 0; width: 268px; height: 428px;
    background: linear-gradient(180deg, #ffffff 40%, var(--panel-grey) 100%);
    border-right: 1px solid var(--divider);
  }
  .back-art { position: absolute; left: 0; top: 0; }
  .back-tagline {
    position: absolute; left: 10px; top: 150px; width: 250px;
    font: 400 16.5px/20.8px "Tinos", "Times New Roman", serif; color: var(--accent-orange);
  }
  .back-tagline__emphasis { color: var(--accent-blue); }
  .back-copy {
    position: absolute; left: 10px; top: 248px; width: 252px;
    font: 400 11.6px/14px "Tinos", "Times New Roman", serif; color: var(--copy-grey);
  }
  .back-serving {
    position: absolute; left: 10px; top: 303px;
    font: 700 12.5px/1 "Tinos", "Times New Roman", serif; color: var(--brand-teal);
    white-space: nowrap;
  }
  .back-contact {
    position: absolute; left: 13px; top: 336px; list-style: none;
    font: 400 13px/20.8px "Tinos", "Times New Roman", serif; color: var(--ink);
    white-space: nowrap;
  }
</style>
</head>
<body>

<section class="postcard postcard--front" aria-label="Postcard front">
  <svg class="front-art" width="553" height="428" viewBox="0 0 553 428">
    <defs>
      <linearGradient id="dartsTone" x1="0" y1="0" x2="1" y2="0">
        <stop offset="0" stop-color="var(--photo-mid)"/>
        <stop offset=".35" stop-color="var(--photo-light)"/>
        <stop offset=".72" stop-color="#f3b06a"/>
        <stop offset=".82" stop-color="var(--photo-dark)"/>
        <stop offset="1" stop-color="#2a1f1a"/>
      </linearGradient>
    </defs>
    <rect width="553" height="428" fill="url(#dartsTone)" role="img" aria-label="Photo of a dartboard with orange darts on a warm orange background"/>
    <path d="M0,278 C150,240 360,250 553,338" fill="none" stroke="var(--curve-band)" stroke-width="9"/>
    <path d="M0,286 C150,250 360,258 553,346 L553,428 L0,428 Z" fill="var(--card-white)"/>
  </svg>
  <h1 class="front-headline">TIRED OF MISSING<br>TARGETS?</h1>
  <p class="front-subline">Hit your target audience<br>with your message today!!!</p>
  <p class="front-offer">1 Month FREE with 1 Year Contract</p>
  <p class="front-call">Call Now!!</p>
  <p class="front-phone">609.555.0148</p>
  <p class="front-web">www.amberlycourier-example.com</p>
  <div class="brand-mark"><span class="brand-mark__dot"></span>The Amberly Courier</div>
</section>

<section class="postcard postcard--back" aria-label="Postcard back">
  <div class="back-panel">
    <svg class="back-art" width="268" height="190" viewBox="0 0 268 190">
      <defs>
        <linearGradient id="officeTone" x1="0" y1="0" x2="1" y2="1">
          <stop offset="0" stop-color="var(--office-light)"/>
          <stop offset=".6" stop-color="#9aa0aa"/>
          <stop offset="1" stop-color="var(--office-dark)"/>
        </linearGradient>
      </defs>
      <path d="M0,0 H268 V185 C180,148 80,132 0,140 Z" fill="url(#officeTone)" role="img" aria-label="Photo of business people meeting in a bright office"/>
      <path d="M0,140 C80,132 180,148 268,185" fill="none" stroke="var(--curve-band)" stroke-width="3"/>
    </svg>
    <p class="back-tagline">We Measure our<br>success according to<br>impact &nbsp;that we have in driving<br>your <span class="back-tagline__emphasis">BUSINESS FORWARD</span></p>
    <p class="back-copy">Lorem ipsum dolor sit amet, consectetuer adipiscing elit, sed diam nonummy nibh euismod tincidunt ut laoreet dolore magna aliquam erat volutpat.</p>
    <p class="back-serving">Serving Hollin County since 1971</p>
    <ul class="back-contact">
      <li>P.O. Box 417, Westbrook Mills, NJ 08652</li>
      <li>Email: info@amberlycourier-example.com</li>
      <li>609.555.0148</li>
      <li>www.amberlycourier-example.com</li>
    </ul>
  </div>
</section>

</body>
</html>
```